Golden Pantry Spice

Distributor of seasonings and spices to the restaurant industry.

Industry/Entity Type

Restaurant

Contact Information for Business Card

Golden Pantry
Derek Hollings
TW Brandvik Distributor
316-487-9021
derek@goldpantryspicehub.com

No minimum order
Gluten & MSG free soup bases

```html
<!DOCTYPE html>
<html lang="en">
<head>
<meta charset="utf-8">
<title>Golden Pantry Spice – Business Card</title>
<link rel="stylesheet" href="https://fonts.googleapis.com/css2?family=Open+Sans:wght@400;600;700&display=swap">
<style>
  :root {
    --backdrop: #e9e6e1;
    --card-white: #ffffff;
    --brand-red: #ee1c1c;
    --brand-red-deep: #c9101a;
    --cocoa: #3b2a24;
    --ink: #2a2a2a;
    --on-red: #ffffff;
  }
  * { box-sizing: border-box; margin: 0; padding: 0; }
  html, body {
    width: 1200px;
    height: 950px;
    overflow: hidden;
    background: var(--backdrop);
    font-family: "Open Sans", Arial, sans-serif;
  }
  .canvas {
    position: relative;
    width: 1200px;
    height: 950px;
  }
  .business-card {
    position: absolute;
    left: 180px;
    top: 235px;
    width: 840px;
    height: 480px;
    background: var(--card-white);
    border-radius: 26px;
    overflow: hidden;
    box-shadow: 0 14px 34px rgba(0, 0, 0, 0.18);
  }
  .accent-panel {
    position: absolute;
    left: 400px;
    top: 250px;
    right: 0;
    bottom: 0;
    background: linear-gradient(160deg, var(--brand-red) 0%, var(--brand-red-deep) 100%);
  }
  .brand-mark {
    position: absolute;
    top: 70px;
    right: 60px;
    display: flex;
    align-items: center;
    gap: 14px;
  }
  .brand-dot {
    width: 30px;
    height: 30px;
    border-radius: 50%;
    background: var(--brand-red);
  }
  .brand-name {
    font-size: 36px;
    font-weight: 600;
    color: var(--cocoa);
    letter-spacing: 0.5px;
  }
  .holder-name {
    position: absolute;
    left: 60px;
    top: 238px;
    font-size: 25px;
    font-weight: 700;
    color: var(--ink);
  }
  .contact-list {
    position: absolute;
    right: 62px;
    bottom: 48px;
    list-style: none;
    color: var(--on-red);
    font-size: 19px;
    line-height: 1.55;
  }
  .contact-item {
    display: flex;
    align-items: center;
    gap: 12px;
  }
  .contact-title { padding-left: 32px; }
  .contact-icon {
    width: 20px;
    height: 20px;
    flex: none;
  }
</style>
</head>
<body>
<main class="canvas">
  <article class="business-card">
    <div class="accent-panel" role="img" aria-label="Decorative curved band in brown, gold and red"></div>

    <div class="brand-mark">
      <span class="brand-dot"></span>
      <span class="brand-name">Golden Pantry Spice</span>
    </div>

    <p class="holder-name">Derek Hollings</p>

    <ul class="contact-list">
      <li class="contact-item contact-title">TW Brandvik Distributor</li>
      <li class="contact-item">
        <svg class="contact-icon" viewBox="0 0 20 20" aria-hidden="true">
          <path d="M5 2 L8 2 L9 6 L7 8 C8 10.5 9.5 12 12 13 L14 11 L18 12 L18 15 C18 16.5 17 17.5 15.5 17.5 C9 17 3 11 2.5 4.5 C2.5 3 3.5 2 5 2 Z" fill="var(--on-red)"/>
        </svg>
        316-487-9021
      </li>
      <li class="contact-item">
        <svg class="contact-icon" viewBox="0 0 20 20" aria-hidden="true">
          <rect x="2" y="4" width="16" height="12" rx="1.5" fill="var(--on-red)"/>
          <path d="M2.5 5 L10 11 L17.5 5" fill="none" stroke="var(--brand-red)" stroke-width="1.6"/>
        </svg>
        derek@goldpantryspicehub.com
      </li>
      <li class="contact-item">
        <svg class="contact-icon" viewBox="0 0 20 20" aria-hidden="true">
          <circle cx="10" cy="10" r="8" fill="none" stroke="var(--on-red)" stroke-width="1.8"/>
          <ellipse cx="10" cy="10" rx="3.5" ry="8" fill="none" stroke="var(--on-red)" stroke-width="1.4"/>
          <path d="M2 10 H18" stroke="var(--on-red)" stroke-width="1.4"/>
        </svg>
        www.goldpantryspicehub.com
      </li>
    </ul>
  </article>
</main>
</body>
</html>
```